■依頼目的 / 概要
電子書籍Lumora本を出版いたしますので、
表紙デザイン作成をお願いいたします。

■納品物
下記での納品をお願い致します。

JPEG形式 及び PSD形式
横1600ピクセル x 縦2560ピクセル

■本の内容

<本のタイトル>
雑貨長者の資金調達術 〜開業ローン篇〜

<サブタイトル>
会社をつくる お金を借りる 原資ができる

<キャッチコピー>
貯金してから起業なんて絶対ダメ!

<著者名>
早川蒼一

■デザイン要望
・本のタイトル / キャッチコピー / 著者名の反映をお願いします

デザインイメージ

・人物や風景の画像を背景にしていただき、
その上にタイトル等コピーを記載

・シンプルな背景にタイトル等のコピーを記載

・資産形成に関する指南書。
その第一歩である新規創業融資に
焦点を当てた内容になっていますが、
お金に関することだけではなく、
人間関係や人生設計にまで
踏み込んだ内容になっています。

・楽して稼ぐといったレベルの低いイメージをもたせるような
デザインにはしたくありません。

<表現したいイメージなど>
・高級感
・かっこいい
・信頼感

<表現したくないイメージ>
・安っぽい
・嘘くさい
・大衆的

<利用画像について>
画像素材を使用される場合には、
商用利用可の素材をお願いします。

■その他
デザインを考えるのに必要な情報が他にございましたら、
お答えしますので、遠慮なくご連絡ください。

数あるご提案の中で、もっとも世界観を表現していただいているものを当選に選ばせていただきました。

この度は、たくさんのご提案ありがとうございました。
レベルの高いご提案が多く、非常に良いデザインを得ることができました。
今回、ご縁がなかったデザイナー様。また次回、ご提案いただければ幸いです。
ありがとうございました!

```html
<!DOCTYPE html>
<html lang="ja">
<head>
<meta charset="UTF-8">
<title>雑貨長者の資金調達術 〜開業ローン篇〜</title>
<link rel="stylesheet" href="https://fonts.googleapis.com/css2?family=Noto+Serif+JP:wght@500;700;900&display=swap">
<style>
  :root {
    --navy: #1e3869;
    --navy-deep: #172d58;
    --grid: rgba(120, 160, 215, 0.28);
    --cream: #ecdcaf;
    --cream-dark: #cdb57a;
    --white: #ffffff;
  }
  html, body { margin: 0; padding: 0; overflow: hidden; }
  body { width: 750px; height: 1200px; }
  .cover {
    position: relative;
    width: 750px;
    height: 1200px;
    overflow: hidden;
    background-color: var(--navy);
    background-image:
      repeating-linear-gradient(0deg, var(--grid) 0 2px, transparent 2px 55px),
      repeating-linear-gradient(90deg, var(--grid) 0 2px, transparent 2px 55px);
    font-family: "Noto Serif JP", serif;
    color: var(--white);
  }
  .catch-frame {
    position: absolute;
    left: 105px; top: 25px;
    width: 540px; height: 140px;
  }
  .catch-frame svg { position: absolute; inset: 0; }
  .catch-copy {
    position: absolute; inset: 0; margin: 0;
    display: flex; flex-direction: column; align-items: center; justify-content: center;
    font-weight: 700; font-size: 36px; line-height: 1.4; letter-spacing: 0.04em;
  }
  .title {
    position: absolute; left: 0; right: 0; top: 192px;
    text-align: center; font-weight: 900; margin: 0;
  }
  .title span { display: block; line-height: 1; }
  .title .lead { font-size: 70px; letter-spacing: 0.02em; }
  .title .middle { font-size: 112px; letter-spacing: 0.08em; margin-top: 22px; }
  .title .main { font-size: 160px; letter-spacing: 0.02em; margin-top: 20px; }
  .volume {
    position: absolute; left: 70px; top: 608px;
    width: 610px; height: 90px;
  }
  .volume svg { position: absolute; inset: 0; }
  .volume-label {
    position: absolute; inset: 0; margin: 0;
    display: flex; align-items: center; justify-content: center;
    color: var(--navy-deep); font-weight: 900; font-size: 50px; line-height: 1; letter-spacing: 0.06em;
    padding-bottom: 6px;
  }
  .compass {
    position: absolute; left: 38px; top: 800px;
    width: 190px; height: 250px;
    border-radius: 50%;
    background: radial-gradient(circle, rgba(205,181,122,0.55) 0%, rgba(205,181,122,0.2) 55%, transparent 72%);
  }
  .promises {
    position: absolute; left: 360px; top: 805px;
    width: 350px; height: 200px;
  }
  .promises svg { position: absolute; left: 0; top: 0; }
  .promise-list {
    list-style: none; margin: 0; padding: 0;
    position: absolute; left: 38px; top: 0;
    font-weight: 700; font-size: 48px; line-height: 66px; letter-spacing: 0.04em;
    white-space: nowrap;
  }
  .promise-list small { font-size: 34px; }
  .author {
    position: absolute; left: 0; right: 0; top: 1075px; margin: 0;
    text-align: center; font-weight: 900; font-size: 56px; line-height: 1; letter-spacing: 0.14em;
  }
</style>
</head>
<body>
<main class="cover">
  <div class="catch-frame">
    <svg width="540" height="140" viewBox="0 0 540 140" aria-hidden="true">
      <path d="M18 4 H522 L536 18 V122 L522 136 H18 L4 122 V18 Z" fill="none" stroke="var(--cream)" stroke-width="3"/>
      <path d="M26 12 H514 L528 26 V114 L514 128 H26 L12 114 V26 Z" fill="none" stroke="var(--cream)" stroke-width="1.5"/>
    </svg>
    <p class="catch-copy"><span>貯金してから起業なんて</span><span>絶対ダメ!</span></p>
  </div>

  <h1 class="title">
    <span class="lead">雑貨長者の</span>
    <span class="middle">資金</span>
    <span class="main">調達術</span>
  </h1>

  <div class="volume">
    <svg width="610" height="90" viewBox="0 0 610 90" aria-hidden="true">
      <path d="M30 14 Q305 2 580 14 L580 74 Q305 62 30 74 Z" fill="var(--cream)" stroke="var(--cream-dark)" stroke-width="3"/>
      <path d="M30 14 Q8 18 10 40 Q12 62 30 74 Q22 58 30 44 Z" fill="var(--cream-dark)"/>
      <path d="M580 14 Q602 18 600 40 Q598 62 580 74 Q588 58 580 44 Z" fill="var(--cream-dark)"/>
    </svg>
    <p class="volume-label">開業ローン篇</p>
  </div>

  <div class="compass" role="img" aria-label="方位を示すコンパスの装飾"></div>

  <div class="promises">
    <svg width="40" height="200" viewBox="0 0 40 200" aria-hidden="true">
      <path d="M30 6 Q14 8 14 28 V80 Q14 96 4 100 Q14 104 14 120 V172 Q14 192 30 194" fill="none" stroke="var(--white)" stroke-width="3"/>
    </svg>
    <ul class="promise-list">
      <li>会社<small>を</small>つくる</li>
      <li>お金<small>を</small>借りる</li>
      <li>原資<small>が</small>できる</li>
    </ul>
  </div>

  <p class="author">早川蒼一</p>
</main>
</body>
</html>
```